Business Card for my Photography/Video Business

I would like the card to say Event Photographer and Videographer. I like the Black and Gold look to it as well but open to other options. I don't want it to be super vibrant or colorful. Simple, elegant and professional

```html
<!DOCTYPE html>
<html lang="en">
<head>
<meta charset="utf-8">
<title>Lumen Frame Business Card</title>
<link rel="stylesheet" href="https://fonts.googleapis.com/css2?family=Roboto:wght@300;400&family=Roboto+Condensed:wght@400&display=swap">
<style>
  :root {
    --backdrop: #e9e6e1;
    --card-dark: #1f2021;
    --card-dark-edge: #2c2d2f;
    --card-light: #fbfbfa;
    --gold: #c9a227;
    --gold-soft: #d8b84a;
    --text-light: #e6e6e6;
    --text-muted: #a9a9a9;
    --text-dark: #555555;
    --rule: #6b6b6b;
  }
  * { box-sizing: border-box; margin: 0; padding: 0; }
  html, body { width: 1200px; height: 911px; overflow: hidden; }
  body {
    background: var(--backdrop);
    font-family: "Roboto", Arial, sans-serif;
    position: relative;
  }
  .card {
    position: absolute;
    width: 520px;
    height: 300px;
    border-radius: 10px;
    box-shadow: 0 10px 30px rgba(0,0,0,0.25);
    overflow: hidden;
  }
  .card-back {
    left: 50px; top: 305px;
    background: linear-gradient(160deg, var(--card-dark-edge) 0%, var(--card-dark) 55%, #151617 100%);
  }
  .card-front {
    left: 630px; top: 305px;
    background: var(--card-light);
  }
  .identity {
    position: absolute;
    left: 70px; top: 118px;
    text-align: right;
    width: 170px;
  }
  .identity-name {
    font-family: "Roboto Condensed", Arial, sans-serif;
    color: var(--gold);
    font-size: 22px;
    letter-spacing: 0.5px;
  }
  .identity-role {
    font-family: "Roboto Condensed", Arial, sans-serif;
    color: var(--text-muted);
    font-size: 14px;
    margin-top: 2px;
  }
  .divider {
    position: absolute;
    left: 262px; top: 100px;
    width: 1px; height: 86px;
    background: var(--rule);
  }
  .contact-list {
    position: absolute;
    left: 284px; top: 96px;
    list-style: none;
  }
  .contact-item {
    display: flex; align-items: center;
    gap: 10px;
    color: var(--text-light);
    font-size: 13px;
    font-weight: 300;
    height: 23px;
  }
  .contact-item svg { width: 12px; height: 12px; flex: none; }
  .address {
    position: absolute;
    right: 30px; bottom: 28px;
    color: var(--text-light);
    font-size: 13px;
    font-weight: 300;
  }
  .brand {
    position: absolute;
    left: 0; right: 0; top: 96px;
    display: flex; align-items: center; justify-content: center;
    gap: 14px;
  }
  .brand-mark {
    width: 62px; height: 62px;
    border-radius: 50%;
    background: var(--gold-soft);
  }
  .brand-name {
    font-size: 40px;
    font-weight: 300;
    color: var(--gold);
    letter-spacing: 3px;
    text-transform: uppercase;
  }
  .website {
    position: absolute;
    left: 0; right: 0; top: 196px;
    text-align: center;
    color: var(--text-dark);
    font-size: 12px;
    letter-spacing: 6px;
  }
</style>
</head>
<body>
  <section class="card card-back">
    <div class="identity">
      <p class="identity-name">EVAN HALE</p>
      <p class="identity-role">CEO/FOUNDER</p>
    </div>
    <div class="divider"></div>
    <ul class="contact-list">
      <li class="contact-item">
        <svg viewBox="0 0 12 12"><path fill="var(--gold)" d="M2.5 1 4.5 3 3.6 4.4c.7 1.6 2.1 3 3.9 3.9L8.9 7.4 11 9.5 9.7 11C5 10.5 1.5 7 1 2.3Z"/></svg>
        <span>555 210 4817</span>
      </li>
      <li class="contact-item">
        <svg viewBox="0 0 12 12"><rect x="3" y="0.5" width="6" height="11" rx="1" fill="none" stroke="var(--gold)"/><circle cx="6" cy="9.5" r="0.7" fill="var(--gold)"/></svg>
        <span>555 382 9064</span>
      </li>
      <li class="contact-item">
        <svg viewBox="0 0 12 12"><rect x="1" y="4" width="10" height="7" rx="1" fill="var(--gold)"/><rect x="3" y="1" width="6" height="3" fill="var(--gold)"/></svg>
        <span>555 774 1326</span>
      </li>
      <li class="contact-item">
        <svg viewBox="0 0 12 12"><rect x="0.5" y="0.5" width="11" height="11" rx="1.5" fill="var(--gold)"/><path d="M3 6.2 5.2 8.3 9 3.8" fill="none" stroke="var(--card-dark)" stroke-width="1.4"/></svg>
        <span>evan@lumenframe.com</span>
      </li>
    </ul>
    <p class="address">1420 Birchwood Road Juneau Alaska 99801</p>
  </section>

  <section class="card card-front">
    <div class="brand">
      <div class="brand-mark"></div>
      <p class="brand-name">Lumen Frame</p>
    </div>
    <p class="website">www.lumenframe.com</p>
  </section>
</body>
</html>
```